Interactive Web Page - Bargain Hollow

Business Name - Bargain Hollow

I would like to create a web site where business' can upload a promotion to sell vouchers for the offer and customers will receive a free coupon which will be an upgrade or bonus.

The idea is to promote businesses in country towns as well as customers getting a great deal for the product or service.

A drop down box with every town and city in Australia to pick from is required.

I want customers to pay using Zentrov. I want a Zentrov payment to then filter to the business selling the offer less a commission which would go to my Zentrov account.

The offers will require a drop down box to choose an expiry date.

The idea is a little like Tallyboons but which some changes.

Industry/Entity Type

Coupon

```html
<!DOCTYPE html>
<html lang="en">
<head>
<meta charset="utf-8">
<title>Bargain Hollow - Premium Coupons And Discounts</title>
<link href="https://fonts.googleapis.com/css2?family=Lato:wght@400;700;900&display=swap" rel="stylesheet">
<style>
:root{
  --orange:#f7890b;
  --ink:#222222;
  --text:#555555;
  --muted:#999999;
  --line:#e6e6e6;
  --paper:#ffffff;
  --soft:#f7f8f8;
  --night:#2b2b2b;
  --night-line:#444444;
  --footer-link:#8a8a8a;
  --search:#333333;
  --green:#9fd28a;
}
*{box-sizing:border-box;margin:0;padding:0}
html,body{width:691px;height:1200px;overflow:hidden}
body{font-family:"Lato",Arial,sans-serif;color:var(--text);background:var(--paper);position:relative}
.brand{display:flex;align-items:center;gap:4px;font-weight:700;color:var(--ink);white-space:nowrap}
.brand-dot{width:7px;height:7px;border-radius:50%;background:var(--orange)}

/* header */
.site-header{position:absolute;top:0;left:0;width:691px;height:44px;background:var(--paper);border-bottom:1px solid var(--line)}
.header-accent{position:absolute;top:0;left:315px;width:59px;height:3px;background:var(--green)}
.site-header .brand{position:absolute;left:81px;top:18px;font-size:13px}
.main-nav{position:absolute;top:17px;left:269px;display:flex;font-size:7px;color:var(--text)}
.main-nav a{color:inherit;text-decoration:none;margin-right:16px}
.main-nav a:last-child{margin-right:0}
.main-nav a.active{color:var(--orange)}
.nav-lock{position:absolute;left:586px;top:16px}

/* hero */
.hero{position:absolute;top:44px;left:0;width:691px;height:354px;overflow:hidden}
.hero-photo{position:absolute;inset:0;background:linear-gradient(180deg,#a8b3a9 0%,#c9b996 40%,#b68e66 70%,#6b5a4d 100%)}
.hero .brand{position:absolute;top:69px;left:50%;transform:translateX(-50%);font-size:13px}
.hero-title{position:absolute;top:97px;left:0;width:691px;text-align:center;font-size:27px;font-weight:900;line-height:28px;color:#fff}
.hero-sub{position:absolute;top:160px;left:0;width:691px;text-align:center;font-size:8.5px;color:#fff}
.search-panel{position:absolute;top:188px;left:173px;width:344px}
.field{height:26px;display:flex;align-items:center;padding:0 11px;font-size:6.5px;gap:7px;position:relative}
.field-city{background:var(--search);color:#eee}
.field-cats{background:var(--paper);color:var(--ink);height:25px}
.field .caret{position:absolute;right:12px;top:10px}
.tabs{position:absolute;top:332px;left:74px;width:520px;height:22px;display:flex}
.tab{flex:1;background:rgba(255,255,255,.85);border-left:1px solid #ccc;font-size:6.5px;color:var(--ink);display:flex;align-items:center;padding-left:9px;position:relative}
.tab .caret{position:absolute;right:10px;top:8px}
.tab.active{background:var(--orange);color:#fff;border-left:none}
.tab.active::after{content:"";position:absolute;left:60px;bottom:-6px;border-left:6px solid transparent;border-right:6px solid transparent;border-top:6px solid var(--orange)}

/* coupons */
.coupon-grid{position:absolute;top:444px;left:83px;width:525px;display:grid;grid-template-columns:repeat(4,121px);column-gap:13.5px;row-gap:16px}
.coupon-card{height:134px;background:var(--paper);border:1px solid var(--line);box-shadow:0 1px 3px rgba(0,0,0,.08);position:relative}
.coupon-image{height:56px;border-bottom:1px solid var(--line);display:flex;justify-content:center;align-items:center}
.coupon-image span{width:28px;height:46px;border-radius:3px 3px 6px 6px;background:linear-gradient(180deg,#3a2418,#7a4a2a 50%,#4a2c1a)}
.badge{position:absolute;top:5px;right:0;background:var(--orange);color:#fff;font-size:5px;padding:2px 5px;letter-spacing:.2px}
.coupon-body{padding:9px 12px 0}
.coupon-title{font-size:7px;font-weight:700;color:var(--ink);margin-bottom:6px}
.coupon-text{font-size:6px;line-height:10.5px;color:var(--text)}
.coupon-meta{position:absolute;left:0;right:0;bottom:0;height:22px;border-top:1px solid var(--line);display:flex;align-items:center;padding:0 12px;font-size:5px;color:var(--muted);gap:7px}
.coupon-meta .add{margin-left:auto;width:7px;height:7px;background:var(--orange);color:#fff;font-size:7px;line-height:7px;text-align:center;font-weight:700}

/* categories */
.extra{position:absolute;top:770px;left:0;width:691px;height:140px;background:var(--soft);border-top:1px solid var(--line)}
.extra-intro{position:absolute;left:83px;top:32px;width:121px}
.extra-intro h2{font-size:11px;font-weight:400;color:var(--ink);padding-bottom:6px;border-bottom:1px solid var(--line);position:relative}
.extra-intro h2::after{content:"";position:absolute;left:0;bottom:-2px;width:23px;height:3px;background:var(--orange)}
.extra-intro p{font-size:6px;color:var(--ink);margin-top:12px}
.btn{display:inline-block;background:var(--orange);color:#fff;font-size:6px;padding:3px 0;text-align:center}
.extra-intro .btn{width:48px;margin-top:6px}
.cat-box{position:absolute;top:33px;width:121px;height:79px;background:var(--paper);border:1px solid var(--line);text-align:center;font-size:8px;color:var(--ink)}
.cat-box svg{display:block;margin:17px auto 9px}

/* footer */
.site-footer{position:absolute;top:910px;left:0;width:691px;height:238px;background:var(--night);color:var(--footer-link)}
.footer-col{position:absolute;top:46px;width:121px}
.footer-col h3{font-size:8px;font-weight:700;color:#fff;margin-bottom:23px}
.footer-col li{list-style:none;font-size:6px;line-height:17px}
.newsletter p{font-size:5.5px;margin-bottom:9px}
.newsletter .email{width:121px;height:16px;border:1px solid var(--night-line);background:#333;color:#ddd;font-size:6px;padding:4px 5px}
.newsletter .btn{width:55px;margin-top:7px}
.social{display:flex;gap:5px;margin-bottom:44px}
.social span{font-size:6px;color:#fff;font-weight:700}
.site-footer .brand{color:#5a5a5a;font-size:11px}
.site-footer .brand-dot{background:#5a5a5a}
.bottom-bar{position:absolute;top:1148px;left:0;width:691px;height:52px;background:var(--paper);font-size:5.5px;color:var(--text)}
.bottom-bar .copy{position:absolute;left:83px;top:22px}
.bottom-nav{position:absolute;left:372px;top:22px;display:flex}
.bottom-nav a{color:inherit;text-decoration:none;margin-right:9px}
.bottom-nav a:last-child{margin-right:0}
.bottom-nav a.active{color:var(--orange)}
</style>
</head>
<body>

<header class="site-header">
  <div class="header-accent"></div>
  <div class="brand">Bargain Hollow <span class="brand-dot"></span></div>
  <nav class="main-nav">
    <a class="active" href="#">Home</a><a href="#">All Shops</a><a href="#">Top 20</a><a href="#">Daily Offers</a><a href="#">Expiring</a><a href="#">Categories</a><a href="#">Contact</a><a href="#">Blog</a>
  </nav>
  <svg class="nav-lock" width="6" height="8" viewBox="0 0 6 8"><rect x="0" y="3.5" width="6" height="4.5" fill="#f7890b"/><path d="M1.2 3.5V2a1.8 1.8 0 0 1 3.6 0" fill="none" stroke="#f7890b" stroke-width="1"/></svg>
</header>

<section class="hero">
  <div class="hero-photo" role="img" aria-label="City skyline at sunset with a tall tower rising on the right"></div>
  <div class="brand">Bargain Hollow <span class="brand-dot"></span></div>
  <h1 class="hero-title">Bargain Hollow - Premium Coupons And<br>Discounts</h1>
  <p class="hero-sub">Over 17 working discount &amp; coupon codes is active for 3 users, enjoy!</p>
  <div class="search-panel">
    <div class="field field-city">
      <svg width="8" height="8" viewBox="0 0 8 8"><circle cx="3.2" cy="3.2" r="2.4" fill="none" stroke="#fff" stroke-width="1.2"/><path d="M5 5l2.5 2.5" stroke="#fff" stroke-width="1.3"/></svg>
      Type City name
      <svg class="caret" width="6" height="4" viewBox="0 0 6 4"><path d="M.5.5l2.5 2.5L5.5.5" fill="none" stroke="#fff"/></svg>
    </div>
    <div class="field field-cats">
      <svg width="7" height="6" viewBox="0 0 7 6"><path d="M0 .5h7M0 3h7M0 5.5h7" stroke="#222"/></svg>
      Categories
      <svg class="caret" width="6" height="4" viewBox="0 0 6 4"><path d="M.5.5l2.5 2.5L5.5.5" fill="none" stroke="#222"/></svg>
    </div>
  </div>
  <div class="tabs">
    <div class="tab active">Featured<svg class="caret" width="6" height="4" viewBox="0 0 6 4"><path d="M.5.5l2.5 2.5L5.5.5" fill="none" stroke="#fff"/></svg></div>
    <div class="tab">Popular<svg class="caret" width="6" height="4" viewBox="0 0 6 4"><path d="M.5.5l2.5 2.5L5.5.5" fill="none" stroke="#333"/></svg></div>
    <div class="tab">Daily Offers<svg class="caret" width="6" height="4" viewBox="0 0 6 4"><path d="M.5.5l2.5 2.5L5.5.5" fill="none" stroke="#333"/></svg></div>
    <div class="tab">Latest<svg class="caret" width="6" height="4" viewBox="0 0 6 4"><path d="M.5.5l2.5 2.5L5.5.5" fill="none" stroke="#333"/></svg></div>
  </div>
</section>

<main class="coupon-grid">
  <article class="coupon-card"><div class="coupon-image"><span role="img" aria-label="Coffee cup product photo"></span></div><div class="badge">FEATURED</div><div class="coupon-body"><h3 class="coupon-title">Coupon 1</h3><p class="coupon-text">Great promo 10% discount code for all products so hurry up...</p></div><div class="coupon-meta"><span>◷ 284 days</span><span>⬖ Discount</span><span class="add">+</span></div></article>
  <article class="coupon-card"><div class="coupon-image"><span role="img" aria-label="Coffee cup product photo"></span></div><div class="badge">FEATURED</div><div class="coupon-body"><h3 class="coupon-title">Coupon 2</h3><p class="coupon-text">Great promo 10% discount code for all products so hurry up...</p></div><div class="coupon-meta"><span>◷ 105 days</span><span>⬖ Coupon</span><span class="add">+</span></div></article>
  <article class="coupon-card"><div class="coupon-image"><span role="img" aria-label="Coffee cup product photo"></span></div><div class="badge">FEATURED</div><div class="coupon-body"><h3 class="coupon-title">Tech Coupon</h3><p class="coupon-text">Great promo 10% discount code for all products so hurry up...</p></div><div class="coupon-meta"><span>◷ 62 days</span><span>⬖ Discount</span><span class="add">+</span></div></article>
  <article class="coupon-card"><div class="coupon-image"><span role="img" aria-label="Coffee cup product photo"></span></div><div class="badge">FEATURED</div><div class="coupon-body"><h3 class="coupon-title">Coupon Computers</h3><p class="coupon-text">Great promo 10% discount code for all products so hurry up...</p></div><div class="coupon-meta"><span>◷ 284 days</span><span>⬖ Coupon</span><span class="add">+</span></div></article>
  <article class="coupon-card"><div class="coupon-image"><span role="img" aria-label="Coffee cup product photo"></span></div><div class="badge">FEATURED</div><div class="coupon-body"><h3 class="coupon-title">Premium Music Box</h3><p class="coupon-text">Great promo 10% discount code for all products so hurry up...</p></div><div class="coupon-meta"><span>◷ 98 days</span><span>⬖ Discount</span><span class="add">+</span></div></article>
  <article class="coupon-card"><div class="coupon-image"><span role="img" aria-label="Coffee cup product photo"></span></div><div class="badge">FEATURED</div><div class="coupon-body"><h3 class="coupon-title">Premium Big</h3><p class="coupon-text">Great promo 10% discount code for all products so hurry up...</p></div><div class="coupon-meta"><span>◷ 98 days</span><span>⬖ Discount</span><span class="add">+</span></div></article>
  <article class="coupon-card"><div class="coupon-image"><span role="img" aria-label="Coffee cup product photo"></span></div><div class="badge">FEATURED</div><div class="coupon-body"><h3 class="coupon-title">Premium Music Box</h3><p class="coupon-text">Great promo 10% discount code for all products so hurry up...</p></div><div class="coupon-meta"><span>◷ 98 days</span><span>⬖ Discount</span><span class="add">+</span></div></article>
  <article class="coupon-card"><div class="coupon-image"><span role="img" aria-label="Coffee cup product photo"></span></div><div class="badge">FEATURED</div><div class="coupon-body"><h3 class="coupon-title">Premium Big</h3><p class="coupon-text">Great promo 10% discount code for all products so hurry up...</p></div><div class="coupon-meta"><span>◷ 98 days</span><span>⬖ Discount</span><span class="add">+</span></div></article>
</main>

<section class="extra">
  <div class="extra-intro">
    <h2>Extra Categories</h2>
    <p>Lorem Ipsum...</p>
    <span class="btn">See All</span>
  </div>
  <div class="cat-box" style="left:218px">
    <svg width="30" height="22" viewBox="0 0 30 22"><rect x="4" y="1" width="22" height="15" rx="1" fill="none" stroke="#222" stroke-width="2"/><path d="M0 19h30v2H0z" fill="#222"/></svg>
    Computers
  </div>
  <div class="cat-box" style="left:352px">
    <svg width="26" height="22" viewBox="0 0 26 22"><path d="M13 1L1 11h3v10h7v-6h4v6h7V11h3z" fill="#222"/></svg>
    House
  </div>
  <div class="cat-box" style="left:486px">
    <svg width="30" height="24" viewBox="0 0 30 24"><rect x="1" y="1" width="28" height="22" fill="none" stroke="#222" stroke-width="2"/><circle cx="9" cy="8" r="3" fill="#222"/><path d="M4 20l8-8 4 4 5-6 5 10z" fill="#222"/></svg>
    Photography
  </div>
</section>

<footer class="site-footer">
  <div class="footer-col newsletter" style="left:83px">
    <h3>Newsletter</h3>
    <p>Latest discounts and coupons</p>
    <div class="email">Email address</div>
    <span class="btn">Subscribe</span>
  </div>
  <div class="footer-col" style="left:218px">
    <h3>FAQ</h3>
    <ul><li>Duis aute irure dolor?</li><li>Sunt in culpa qui officia?</li><li>Cillum dolore eu fugiat?</li><li>Lorem Ipsum dolor sit?</li><li>Dolor Sit Amet?</li><li>Set Do Eiusmod?</li><li>Excepteur sint occaecat?</li></ul>
  </div>
  <div class="footer-col" style="left:352px">
    <h3>About Us</h3>
    <ul><li>Sed ut perspiciatis unde</li><li>Omnis iste natus error</li><li>Sit voluptatem accusantium</li><li>Doloremque laudantium</li><li>Totam rem aperiameaque</li><li>Ipsa quae ab illo inventore veritatis</li></ul>
  </div>
  <div class="footer-col" style="left:486px">
    <h3>Follow Us</h3>
    <div class="social"><span>Chirpline</span><span>Friendwall</span><span>Circlenet</span></div>
    <div class="brand">Bargain Hollow <span class="brand-dot"></span></div>
  </div>
</footer>

<div class="bottom-bar">
  <span class="copy">All rights reserved 2014</span>
  <nav class="bottom-nav">
    <a class="active" href="#">Home</a><a href="#">All Shops</a><a href="#">Top 20</a><a href="#">Daily Offers</a><a href="#">Expiring</a><a href="#">Categories</a><a href="#">Contact</a><a href="#">Blog</a>
  </nav>
</div>

</body>
</html>
```